Telecommunications/Power civil contractor needs business card design

Were a new telecommunications/power underground civil contractor that is looking for a new business card design. Our company colours are silver or grey and orange. Feel free to use the white background logo or the black background logo.

Target Market(s)

Local contractors, utility companies, private sector mining/energy companies, developers.

Industry/Entity Type

Telecommunications

Contact Information for Business Card

Each card will need the following info:
Persons name:
Title:
E-mail:
Phone number:
Shop Address:
Mailing Address:

Requirements
Must have
• Each card will need the following info:
• Persons name:
• Title:
• E-mail:
• Phone number:
• Shop Address:
• Mailing Address:

```html
<!DOCTYPE html>
<html lang="en">
<head>
<meta charset="utf-8">
<title>Tapline Contracting Inc – Business Card</title>
<link rel="stylesheet" href="https://fonts.googleapis.com/css2?family=Lato:wght@400;700;900&display=swap">
<style>
  :root {
    --backdrop: #2b2b2b;
    --card-black: #0c0c0c;
    --card-white: #f4f4f4;
    --orange: #e2541b;
    --grey: #8a8a8a;
    --ink: #1a1a1a;
  }
  * { box-sizing: border-box; margin: 0; padding: 0; }
  html, body { width: 1200px; height: 873px; overflow: hidden; }
  body {
    background: var(--backdrop);
    font-family: "Lato", sans-serif;
    display: flex;
    align-items: center;
    justify-content: center;
  }
  .business-card {
    width: 840px;
    height: 480px;
    border-radius: 26px;
    overflow: hidden;
    display: flex;
    background: var(--card-white);
    box-shadow: 0 20px 50px rgba(0,0,0,.5);
  }
  .brand-panel {
    width: 372px;
    background: var(--card-black);
    display: flex;
    align-items: center;
    justify-content: center;
    gap: 18px;
  }
  .brand-dot {
    width: 26px;
    height: 26px;
    border-radius: 50%;
    background: var(--orange);
    flex: none;
  }
  .brand-name {
    color: var(--orange);
    font-weight: 900;
    font-size: 34px;
    line-height: 1.1;
    letter-spacing: 1px;
    text-transform: uppercase;
  }
  .divider-stripes {
    width: 30px;
    display: flex;
    background: var(--card-white);
  }
  .divider-stripes span { flex: 1; }
  .divider-stripes span:nth-child(odd) { background: var(--card-black); }
  .contact-panel {
    flex: 1;
    padding: 62px 0 0 58px;
    color: var(--ink);
  }
  .person-name {
    color: var(--orange);
    font-weight: 700;
    font-size: 25px;
  }
  .person-title {
    font-size: 17px;
    font-weight: 700;
    margin-top: 3px;
  }
  .contact-list { list-style: none; margin-top: 44px; }
  .contact-line {
    display: flex;
    align-items: center;
    gap: 14px;
    font-size: 19px;
    margin-bottom: 14px;
  }
  .contact-line svg { width: 22px; height: 22px; flex: none; fill: var(--orange); }
  .address { margin: 26px 0 0 36px; }
  .address + .address { margin-top: 24px; }
  .address-street {
    color: var(--orange);
    font-weight: 700;
    font-size: 20px;
    line-height: 1.2;
  }
  .address-label { font-size: 18px; margin-top: 3px; }
</style>
</head>
<body>
  <article class="business-card">
    <section class="brand-panel">
      <span class="brand-dot"></span>
      <div class="brand-name">Tapline<br>Contracting Inc</div>
    </section>
    <div class="divider-stripes"><span></span><span></span><span></span><span></span><span></span></div>
    <section class="contact-panel">
      <h1 class="person-name">Daniel Harlow</h1>
      <p class="person-title">Chief Operating Officer</p>
      <ul class="contact-list">
        <li class="contact-line">
          <svg viewBox="0 0 24 24" aria-hidden="true"><path d="M6.6 10.8a15.1 15.1 0 0 0 6.6 6.6l2.2-2.2a1 1 0 0 1 1-.25 11.4 11.4 0 0 0 3.6.57 1 1 0 0 1 1 1V20a1 1 0 0 1-1 1A17 17 0 0 1 3 4a1 1 0 0 1 1-1h3.5a1 1 0 0 1 1 1c0 1.25.2 2.45.57 3.57a1 1 0 0 1-.25 1z"/></svg>
          412-555-0147
        </li>
        <li class="contact-line">
          <svg viewBox="0 0 24 24" aria-hidden="true"><path d="M2 5h20v14H2z M3.5 6.5 12 13l8.5-6.5" fill="var(--orange)"/><path d="M3.5 6.5 12 13l8.5-6.5" fill="none" stroke="#fff" stroke-width="1.6"/></svg>
          enquiries@taplinecontracting.com
        </li>
      </ul>
      <div class="address">
        <p class="address-street">#1480 Ashford Avenue,<br>Cedarville, New York</p>
        <p class="address-label">(Mailling Address)</p>
      </div>
      <div class="address">
        <p class="address-street">52 Harmon Drive,<br>Lakefield, PA 15100</p>
        <p class="address-label">(Shop Address)</p>
      </div>
    </section>
  </article>
</body>
</html>
```